Web Design for Financial Consulting Company

We need a website design for a financial consulting company "Kelvane Consulting". We build financial models, scenario analysis, handle the budgeting process and provide temporary staffing. I have over 10 years of experience. My Excel expertise and analytical savvy has saved clients over $17 million in profit.

Target Market(s)

Small to medium businesses

Industry/Entity Type

Financial Consulting

Number of Pages Required

4 page

Requirements
Must have
• Professional looking
Nice to have
• A little futuristic looking

```html
<!DOCTYPE html>
<html lang="en">
<head>
<meta charset="utf-8">
<title>Kelvane Consulting</title>
<link rel="stylesheet" href="https://fonts.googleapis.com/css2?family=Poppins:wght@300;400;500;600;700;800&display=swap">
<style>
:root{
  --blue:#0aa8f2;
  --navy:#05426f;
  --navy-deep:#073a63;
  --ink:#0b3c66;
  --text:#4a4a4a;
  --white:#ffffff;
  --field:#e3e6ea;
}
*{margin:0;padding:0;box-sizing:border-box}
html,body{width:1200px;height:2734px;overflow:hidden}
body{position:relative;font-family:"Poppins",sans-serif;background:var(--white);color:var(--text)}
.abs{position:absolute}
/* header */
.site-header{position:absolute;left:0;top:0;width:1200px;height:90px;background:var(--white)}
.brand{position:absolute;display:flex;align-items:center;gap:10px}
.brand-mark{width:30px;height:30px;background:var(--blue)}
.brand-name{font-weight:700;font-size:30px;letter-spacing:1px;color:var(--ink);line-height:1}
.brand-sub{font-size:10px;letter-spacing:13px;color:var(--blue);font-weight:500;margin-top:2px}
.topbar-mail{left:589px;top:0;width:292px;height:34px;background:var(--navy-deep);clip-path:polygon(0 0,100% 0,100% 100%,28px 100%);color:#fff;font-size:13.5px;display:flex;align-items:center;padding-left:42px;gap:10px}
.topbar-call{left:881px;top:0;width:258px;height:34px;background:var(--blue);clip-path:polygon(0 0,100% 0,calc(100% - 22px) 100%,0 100%);color:#fff;font-size:15px;font-weight:500;display:flex;align-items:center;padding-left:20px;gap:10px}
.main-nav{left:773px;top:54px;display:flex;gap:37px;font-size:12.5px;color:#111;font-weight:400}
.main-nav .active{color:var(--blue)}
/* hero */
.hero{left:0;top:90px;width:1200px;height:614px;background:linear-gradient(120deg,#243f5c 0%,#3d5c7c 45%,#7d95ad 100%);overflow:hidden}
.hero-title{left:58px;top:322px;font-size:47px;font-weight:700;line-height:60px;color:#fff;text-transform:uppercase}
.hero-title span{color:var(--blue)}
.btn{background:var(--blue);color:#fff;font-weight:600;text-transform:uppercase;display:flex;align-items:center;justify-content:center}
.hero-btn{left:58px;top:511px;width:141px;height:42px;font-size:15px;border:1px solid #fff}
.slide-arrow{left:1097px;width:42px;height:42px;border-radius:50%;background:rgba(255,255,255,.35);display:flex;align-items:center;justify-content:center}
/* about */
.about-photo{background:linear-gradient(135deg,#355c86,#8fa8c4)}
.about-photo.front{background:linear-gradient(135deg,#eef1f4,#c9d0d8 60%,#3c4f68)}
.about-title{left:636px;top:818px;font-size:40px;font-weight:700;color:var(--ink);text-transform:uppercase}
.about-sub{left:636px;top:871px;font-size:19px;color:var(--blue);text-transform:uppercase}
.about-text{left:636px;top:916px;width:380px;font-size:14px;line-height:24px;color:#555}
.benefits{left:634px;top:1066px;list-style:none}
.benefits li{display:flex;align-items:center;gap:14px;height:32.3px;font-size:14.5px;color:var(--ink)}
/* services */
.services{left:0;top:1312px;width:1200px;height:473px;background:var(--navy)}
.eyebrow{font-size:19px;color:var(--blue);text-transform:uppercase}
.services-title{left:62px;top:1415px;font-size:35px;font-weight:700;line-height:40px;color:#fff;text-transform:uppercase}
.service{top:1538px;width:200px;height:179px}
.service h3{position:absolute;top:80px;font-size:16.5px;font-weight:600;line-height:26px;color:#fff;text-transform:uppercase}
.service .more{position:absolute;top:154px;display:flex;align-items:center;gap:10px;font-size:14px;color:var(--blue)}
.divider{top:1538px;width:1px;height:179px;background:rgba(255,255,255,.2)}
/* contact */
.contact{left:0;top:1785px;width:1200px;height:652px;background:linear-gradient(180deg,#f4f5f7,#fff 40%)}
.contact-visual{left:640px;top:1945px;width:500px;height:492px;background:linear-gradient(160deg,#0aa8f2 0%,#2a4f8c 55%,#e9edf2 100%)}
.contact-title{left:0;top:1850px;width:1200px;text-align:center;font-size:36px;font-weight:700;color:var(--ink);text-transform:uppercase;z-index:2}
.contact-sub{left:0;top:1902px;width:1200px;text-align:center;font-size:15px;color:#555;z-index:2}
.field{left:60px;width:487px;height:42px;background:#fff;border:1px solid var(--field);box-shadow:0 2px 6px rgba(0,0,0,.06);font-size:11.5px;color:#555;padding:0 15px;display:flex;align-items:center}
.field.focus{border-color:var(--blue)}
.field.area{align-items:flex-start;padding-top:16px}
.submit{left:65px;top:2318px;width:101px;height:40px;font-size:15px}
/* footer */
.site-footer{left:0;top:2437px;width:1200px;height:253px;background:var(--navy)}
.footer-head{font-size:15px;font-weight:600;color:#fff;text-transform:uppercase}
.footer-list{list-style:none;font-size:13.5px;color:#fff}
.footer-list li{height:26.4px;display:flex;align-items:center;gap:10px}
.footer-list li::before{content:"";width:5px;height:5px;border-radius:50%;background:var(--blue)}
.social{top:2569px;width:38px;height:38px;border:1px solid var(--blue)}
.contact-line{left:888px;display:flex;gap:14px;font-size:13.5px;color:#fff;line-height:20px}
.copyright{left:0;top:2690px;width:1200px;height:44px;background:var(--blue);color:#fff;font-size:12px;display:flex;align-items:center;justify-content:center}
</style>
</head>
<body>

<header class="site-header">
  <div class="brand" style="left:59px;top:24px">
    <div class="brand-mark"></div>
    <div><div class="brand-name">KELVANE</div><div class="brand-sub">CONSULTING</div></div>
  </div>
  <div class="abs topbar-mail">
    <svg width="22" height="16" viewBox="0 0 22 16" fill="none" stroke="#0aa8f2" stroke-width="1.5"><rect x="1" y="1" width="20" height="14"/><path d="M1 1l10 8 10-8"/></svg>
    info@kelvaneconsulting.com
  </div>
  <div class="abs topbar-call">
    <svg width="22" height="22" viewBox="0 0 24 24" fill="none" stroke="#073a63" stroke-width="1.6"><path d="M5 3h4l2 5-3 2a11 11 0 0 0 6 6l2-3 5 2v4a2 2 0 0 1-2 2A17 17 0 0 1 3 5a2 2 0 0 1 2-2z"/></svg>
    Call Us: 123 555 0147
  </div>
  <nav class="abs main-nav">
    <span class="active">▮ HOME</span><span>ABOUT US</span><span>SERVICES</span><span>CONTACT US</span>
  </nav>
</header>

<section class="abs hero">
  <div class="abs" style="inset:0" role="img" aria-label="Photo of a finance team reviewing a financial dashboard on a monitor"></div>
  <svg class="abs" style="left:0;top:0" width="1200" height="614" viewBox="0 0 1200 614">
    <polygon points="0,0 380,0 0,470" fill="rgba(8,50,95,.45)"/>
    <polygon points="0,614 430,614 0,420" fill="#0aa8f2" opacity=".85"/>
  </svg>
</section>
<h1 class="abs hero-title">Helping your<br>finance team and<br><span>increasing profit</span></h1>
<div class="abs btn hero-btn">Get Started</div>
<div class="abs slide-arrow" style="top:344px"><svg width="22" height="14" viewBox="0 0 22 14" fill="none" stroke="#fff" stroke-width="1.8"><path d="M1 7h19M14 1l6 6-6 6"/></svg></div>
<div class="abs slide-arrow" style="top:393px"><svg width="22" height="14" viewBox="0 0 22 14" fill="none" stroke="#fff" stroke-width="1.8"><path d="M21 7H2M8 1L2 7l6 6"/></svg></div>

<div class="abs about-photo" style="left:114px;top:780px;width:322px;height:374px" role="img" aria-label="Photo of a smiling consultant presenting"></div>
<div class="abs about-photo front" style="left:242px;top:890px;width:321px;height:344px" role="img" aria-label="Photo of a consultant discussing charts on a laptop"></div>
<h2 class="abs about-title">About Kelvane</h2>
<div class="abs about-sub">Consulting</div>
<p class="abs about-text">I am an experienced Finance professional who develops strategic financial plans, provides insightful analysis, and supports decision-making. With over 10 years of experience, I have successfully increased profitability for clients by $17M.</p>
<ul class="abs benefits">
  <li><svg width="18" height="18" viewBox="0 0 18 18" fill="none" stroke="#0aa8f2" stroke-width="1.6"><circle cx="8" cy="10" r="7"/><path d="M5 9l3 3 8-9"/></svg>Save time and energy</li>
  <li><svg width="18" height="18" viewBox="0 0 18 18" fill="none" stroke="#0aa8f2" stroke-width="1.6"><circle cx="8" cy="10" r="7"/><path d="M5 9l3 3 8-9"/></svg>Great support &amp; services</li>
  <li><svg width="18" height="18" viewBox="0 0 18 18" fill="none" stroke="#0aa8f2" stroke-width="1.6"><circle cx="8" cy="10" r="7"/><path d="M5 9l3 3 8-9"/></svg>Risk reduction</li>
  <li><svg width="18" height="18" viewBox="0 0 18 18" fill="none" stroke="#0aa8f2" stroke-width="1.6"><circle cx="8" cy="10" r="7"/><path d="M5 9l3 3 8-9"/></svg>Peace of mind</li>
</ul>

<section class="abs services"></section>
<div class="abs eyebrow" style="left:62px;top:1383px">Services</div>
<h2 class="abs services-title">Your business goal are<br>our priority</h2>

<div class="abs service" style="left:62px">
  <svg width="62" height="60" viewBox="0 0 62 60" fill="none" stroke="#0aa8f2" stroke-width="1.8"><circle cx="10" cy="10" r="8"/><rect x="24" y="6" width="26" height="22"/><circle cx="22" cy="34" r="11"/><path d="M30 42l8 8"/><rect x="40" y="30" width="20" height="28"/><path d="M44 36h12M44 44h12M44 50h12"/></svg>
  <h3>Financial Models<br>Projects</h3>
  <div class="more">Read More <svg width="22" height="12" viewBox="0 0 22 12" fill="none" stroke="#0aa8f2" stroke-width="1.6"><path d="M0 6h20M15 1l5 5-5 5"/></svg></div>
</div>
<div class="abs divider" style="left:254px"></div>
<div class="abs service" style="left:283px">
  <svg width="56" height="60" viewBox="0 0 56 60" fill="none" stroke="#fff" stroke-width="1.8"><rect x="2" y="2" width="32" height="46"/><path d="M10 12h18M10 20h18M10 28h12M10 36h10"/><circle cx="40" cy="44" r="12"/><circle cx="40" cy="44" r="5"/></svg>
  <h3>Budgeting<br>Process</h3>
  <div class="more"><svg width="22" height="12" viewBox="0 0 22 12" fill="none" stroke="#0aa8f2" stroke-width="1.6"><path d="M0 6h20M15 1l5 5-5 5"/></svg></div>
</div>
<div class="abs divider" style="left:476px"></div>
<div class="abs service" style="left:505px">
  <svg width="60" height="60" viewBox="0 0 60 60" fill="none" stroke="#fff" stroke-width="1.8"><circle cx="30" cy="20" r="15"/><circle cx="30" cy="20" r="6"/><path d="M2 58V46a8 8 0 0 1 16 0v12M22 58V44a8 8 0 0 1 16 0v14M42 58V46a8 8 0 0 1 16 0v12"/></svg>
  <h3>Temporary<br>Staffing</h3>
  <div class="more"><svg width="22" height="12" viewBox="0 0 22 12" fill="none" stroke="#0aa8f2" stroke-width="1.6"><path d="M0 6h20M15 1l5 5-5 5"/></svg></div>
</div>
<div class="abs divider" style="left:698px"></div>
<div class="abs service" style="left:727px">
  <svg width="60" height="60" viewBox="0 0 60 60" fill="none" stroke="#fff" stroke-width="1.8"><path d="M14 2v40M6 58l8-16 8 16z"/><rect x="26" y="28" width="28" height="8"/><rect x="26" y="38" width="28" height="8"/><rect x="26" y="48" width="28" height="8"/><circle cx="46" cy="12" r="7"/></svg>
  <h3>Data<br>Cleansing</h3>
  <div class="more"><svg width="22" height="12" viewBox="0 0 22 12" fill="none" stroke="#0aa8f2" stroke-width="1.6"><path d="M0 6h20M15 1l5 5-5 5"/></svg></div>
</div>
<div class="abs divider" style="left:919px"></div>
<div class="abs service" style="left:949px">
  <svg width="58" height="60" viewBox="0 0 58 60" fill="none" stroke="#fff" stroke-width="1.8"><circle cx="22" cy="38" r="16"/><circle cx="22" cy="38" r="6"/><path d="M34 20V4l-6 6M34 4l6 6M46 24V12"/><circle cx="42" cy="46" r="9"/><path d="M42 41v5h4"/></svg>
  <h3>Process<br>Improvement</h3>
  <div class="more"><svg width="22" height="12" viewBox="0 0 22 12" fill="none" stroke="#0aa8f2" stroke-width="1.6"><path d="M0 6h20M15 1l5 5-5 5"/></svg></div>
</div>

<section class="abs contact"></section>
<div class="abs contact-visual" role="img" aria-label="Photo of a smiling consultant holding a laptop in front of a blue rising bar graphic"></div>
<h2 class="abs contact-title">Contact Us</h2>
<p class="abs contact-sub">If you have an any question for contact us today!</p>
<div class="abs field focus" style="top:1972px">First Name *</div>
<div class="abs field" style="top:2031px">Last Name *</div>
<div class="abs field" style="top:2090px">Email *</div>
<div class="abs field" style="top:2148px;justify-content:space-between">Subject * <svg width="10" height="6" viewBox="0 0 10 6"><path d="M0 0h10L5 6z" fill="#0b3c66"/></svg></div>
<div class="abs field area" style="top:2205px;height:97px">Comment or Message *</div>
<div class="abs btn submit">Submit</div>

<footer class="abs site-footer"></footer>
<div class="brand" style="left:59px;top:2504px">
  <div class="brand-mark"></div>
  <div><div class="brand-name" style="color:#fff">KELVANE</div><div class="brand-sub">CONSULTING</div></div>
</div>
<div class="abs social" style="left:115px"></div>
<div class="abs social" style="left:162px"></div>
<div class="abs social" style="left:209px"></div>

<div class="abs footer-head" style="left:351px;top:2480px">Quick Links</div>
<ul class="abs footer-list" style="left:351px;top:2513px">
  <li>Home</li><li>About</li><li>Services</li><li>Contact</li>
</ul>
<div class="abs footer-head" style="left:604px;top:2480px">Services</div>
<ul class="abs footer-list" style="left:604px;top:2513px">
  <li>Financial Models – Projects</li><li>Budgeting Process</li><li>Temporary Staffing</li><li>Data cleansing</li><li>Process Improvement</li>
</ul>
<div class="abs footer-head" style="left:888px;top:2480px">Get in Touch</div>
<div class="abs contact-line" style="top:2517px">
  <svg width="20" height="26" viewBox="0 0 20 26" fill="none" stroke="#0aa8f2" stroke-width="1.5"><path d="M10 25S2 15 2 9a8 8 0 0 1 16 0c0 6-8 16-8 16z"/><circle cx="10" cy="9" r="3"/></svg>
  <span>101 - kelvane consulting<br>lorem ipsum simple text print</span>
</div>
<div class="abs contact-line" style="top:2578px">
  <svg width="22" height="22" viewBox="0 0 24 24" fill="none" stroke="#0aa8f2" stroke-width="1.5"><path d="M5 3h4l2 5-3 2a11 11 0 0 0 6 6l2-3 5 2v4a2 2 0 0 1-2 2A17 17 0 0 1 3 5a2 2 0 0 1 2-2z"/></svg>
  <span>123 555 0147</span>
</div>
<div class="abs contact-line" style="top:2616px">
  <svg width="22" height="18" viewBox="0 0 22 16" fill="none" stroke="#0aa8f2" stroke-width="1.5"><rect x="1" y="1" width="20" height="14"/><path d="M1 1l10 8 10-8"/></svg>
  <span>info@kelvaneconsulting.com</span>
</div>
<div class="abs copyright">©KELVANE CONSULTING - 2023 All rights reserved.</div>

</body>
</html>
```